Outdoor Sign - Slight Redesign

We are wanting to redesign our outdoor sign. Do not change the logos. The background images behind the Lantrel and Corvex are a bit off and we would like different options. Wanting to display professionalism and boldness.
Updates

Target Market(s)

Oil and gas

Industry/Entity Type

Oil and gas

Requirements
Must have
• Use the same logo I uploaded. Please adjust the background image.
Should not have
• Do not start something new. Use what I have

```html
<!DOCTYPE html>
<html lang="en">
<head>
<meta charset="utf-8">
<title>Lantrel &amp; Corvex Outdoor Sign</title>
<link href="https://fonts.googleapis.com/css2?family=Montserrat:wght@500;600;700;800&display=swap" rel="stylesheet">
<style>
  :root {
    --canvas-grey: #cfcfcf;
    --band-gold: #e6d283;
    --stripe-gold: #e3cf85;
    --asphalt-dark: #161a22;
    --asphalt-mid: #2c323d;
    --texture-dark: #1c1c1c;
    --texture-mid: #3a3a3a;
    --ink: #0d0d0d;
    --white: #ffffff;
    --cream: #f1e6bd;
    --ring-tan: #a8916f;
    --badge-dark: #141414;
  }
  * { margin: 0; padding: 0; box-sizing: border-box; }
  html, body {
    width: 1111px;
    height: 1200px;
    overflow: hidden;
    background: var(--canvas-grey);
    font-family: "Montserrat", sans-serif;
  }
  .sign {
    position: absolute;
    left: 115px;
    top: 380px;
    width: 881px;
    height: 440px;
    background: var(--band-gold);
    overflow: hidden;
  }
  .sign-art {
    position: absolute;
    left: 0;
    top: 0;
    width: 881px;
    height: 328px;
  }
  .brand {
    position: absolute;
    text-align: center;
    line-height: 1;
  }
  .brand-lantrel {
    left: 60px;
    top: 118px;
    width: 340px;
    color: var(--white);
    font-weight: 800;
  }
  .brand-lantrel .brand-name { font-size: 58px; letter-spacing: 1px; }
  .brand-lantrel .brand-sub { font-size: 16px; letter-spacing: 3px; margin-top: 10px; }
  .brand-corvex {
    left: 520px;
    top: 218px;
    width: 310px;
    color: var(--cream);
    font-weight: 800;
  }
  .brand-corvex .brand-name { font-size: 54px; letter-spacing: 2px; }
  .brand-corvex .brand-sub { font-size: 23px; letter-spacing: 4px; margin-top: 12px; }
  .contact {
    position: absolute;
    left: 0;
    top: 328px;
    width: 881px;
    height: 112px;
    text-align: center;
    color: var(--ink);
  }
  .contact-address {
    position: absolute;
    left: 0;
    width: 100%;
    top: 10px;
    font-size: 36px;
    font-weight: 600;
  }
  .contact-phone {
    position: absolute;
    left: 0;
    width: 100%;
    top: 51px;
    font-size: 47px;
    font-weight: 700;
  }
  .rules {
    position: absolute;
    width: 190px;
    height: 40px;
    top: 382px;
  }
  .rules-left { left: 21px; }
  .rules-right { left: 670px; }
</style>
</head>
<body>
  <main class="sign">
    <svg class="sign-art" viewBox="0 0 881 328" xmlns="http://www.w3.org/2000/svg">
      <defs>
        <linearGradient id="asphalt" x1="0" y1="0" x2="1" y2="1">
          <stop offset="0" stop-color="var(--asphalt-mid)"/>
          <stop offset="0.5" stop-color="var(--asphalt-dark)"/>
          <stop offset="1" stop-color="var(--asphalt-mid)"/>
        </linearGradient>
        <linearGradient id="texture" x1="0" y1="0" x2="1" y2="1">
          <stop offset="0" stop-color="var(--texture-dark)"/>
          <stop offset="0.6" stop-color="var(--texture-mid)"/>
          <stop offset="1" stop-color="var(--texture-dark)"/>
        </linearGradient>
      </defs>
      <polygon class="divider-stripe" points="521,0 543,0 423,328 395,328" fill="var(--stripe-gold)"/>
      <path class="panel-left" role="img" aria-label="Photo of wet cracked asphalt" d="M0 0 H522 L418 286 Q403 328 360 328 H0 Z" fill="url(#asphalt)"/>
      <polygon class="panel-right" role="img" aria-label="Photo of dark textured oil-coated surface" points="543,0 881,0 881,328 423,328" fill="url(#texture)"/>
      <circle class="corvex-circle" cx="672" cy="114" r="82" fill="var(--badge-dark)" stroke="var(--ring-tan)" stroke-width="6"/>
    </svg>

    <div class="brand brand-lantrel">
      <div class="brand-name">LANTREL</div>
      <div class="brand-sub">PRODUCTION SERVICES</div>
    </div>

    <div class="brand brand-corvex">
      <div class="brand-name">CORVEX</div>
      <div class="brand-sub">DOWNHOLE LLC</div>
    </div>

    <section class="contact">
      <p class="contact-address">4820 WEST COUNTY ROAD 61</p>
      <p class="contact-phone">(432) 555 0147</p>
    </section>

    <svg class="rules rules-left" viewBox="0 0 190 40" xmlns="http://www.w3.org/2000/svg">
      <rect x="0" y="0" width="70" height="7" fill="var(--white)"/>
      <rect x="0" y="15" width="190" height="7" fill="var(--white)"/>
      <rect x="0" y="31" width="190" height="7" fill="var(--white)"/>
    </svg>
    <svg class="rules rules-right" viewBox="0 0 190 40" xmlns="http://www.w3.org/2000/svg">
      <rect x="120" y="0" width="70" height="7" fill="var(--white)"/>
      <rect x="0" y="15" width="190" height="7" fill="var(--white)"/>
      <rect x="0" y="31" width="190" height="7" fill="var(--white)"/>
    </svg>
  </main>
</body>
</html>
```